Book Cover Design | Science & Nature

We are looking for a cover design for our new educational book titled "Moths Beyond the Hedge".
The full title on the cover can either only be "Moths Beyond the Hedge" or "Garden Moths Beyond the Hedge - a pocket handbook". Up to you what looks good. If the latter, the words "Moths Beyond the Hedge" should be written in larger letters.
The book has a lot information about spiders in general and provides a convenient and understandable identification guide about spiders in California.
The target audience are normal, non-scientist readers who would like to get a simple guide that helps them identify common spiders they will find inside their homes and gardens.
The book is written in an understandable, non-scientific language and contains numerous illustrations and identification sheets of all common spiders.
We are fairly open to suggestions about the design. It should not be too plain as it is not a classic boring science book, but aimed at the average reader. Readers are both male and female, aged 30 and above.
If you know nothing about spiders but would like to know what the spiders in your backyard are, which ones are dangerous and if you want to learn more about spiders, this should be the book you will want to buy!
The author is Dale Prowse. In addition to the author, the book cover should show "Brindlewing.com" - The author can be at the bottom and the website on the top or vice versa.
The cover size is 6" x 9" (15.24 x 22.86 cm). The book has around 150 pages. The back of the book should have a placeholder for the barcode as well as some text. It should also have a quick overview of the main benefits of the book: Easily understandable for non-scientist readers, helpful illustrations, tips on how to deal with spiders in the house and with spider bites. We will obviously add the text later.
I've attached a few of the illustrations as I think they could be used to already give the reader a feeling what they will get with the book. If you think a stock photo will work better than the illustrations, that is fine too.

Target Market(s)

Average readers in the United States wanting to learn more about spiders

Industry/Entity Type

Science, Nature, Spiders, Animals, Education

Requirements
Must have
• When the artwork is generated, the files we would like to receive are: The original working file PSD (Photoshop Document - so any text and images can be edited) All the working elements including: illustrations, photos, graphics and fonts A high resolution (300 dpi), 8.5 x 11 (o- Once r larger) file A JPG file in the exact size specifications and color required by our publisher A JPG file in the exact size for online POD or ebook (Pagelume requires 900x600 ) A JPG black and white (gray scale) variation
Nice to have
• A text (overlay?) could point out some of the advantages of this book: Illustrations and identification guides for all common California spiders, tips on how to get rid of spiders from inside the house, tips on how to deal with arachnophobia, etc. This is optional. Maybe something like "An easy to understand identification guide with plenty of tips and illustrations".
Should not have
• Very dark colors or very feminine colors or shapes.

```html
<!DOCTYPE html>
<html lang="en">
<head>
<meta charset="utf-8">
<title>Moths Beyond the Hedge – Book Cover</title>
<link rel="stylesheet" href="https://fonts.googleapis.com/css2?family=Archivo+Black&family=Nunito+Sans:wght@400;600&family=Caveat:wght@400&display=swap">
<style>
  :root {
    --sky-light: #86c8f0;
    --sky-mid: #4fa6dd;
    --sky-deep: #3a62c8;
    --leaf-light: #a6d24a;
    --leaf-mid: #6aa52f;
    --leaf-dark: #2f5f22;
    --creature-dark: #1e1a14;
    --creature-gold: #e2c23a;
    --crimson: #b81232;
    --white: #ffffff;
  }
  * { margin: 0; padding: 0; box-sizing: border-box; }
  html, body { width: 805px; height: 1200px; overflow: hidden; background: var(--white); }
  .cover {
    position: relative;
    width: 805px;
    height: 1200px;
    overflow: hidden;
    font-family: "Nunito Sans", "Avenir Next", sans-serif;
    color: var(--white);
  }
  .cover-art {
    position: absolute;
    inset: 0 0 153px 0;
    background:
      radial-gradient(ellipse 230px 200px at 400px 520px, rgba(150,210,245,0.9) 0%, rgba(134,200,240,0) 100%),
      radial-gradient(ellipse 300px 420px at 720px 330px, var(--leaf-dark) 0%, rgba(47,95,34,0) 100%),
      radial-gradient(ellipse 360px 300px at 620px 200px, var(--leaf-mid) 0%, rgba(106,165,47,0) 100%),
      radial-gradient(ellipse 200px 260px at 90px 330px, var(--leaf-light) 0%, rgba(166,210,74,0) 100%),
      radial-gradient(ellipse 180px 150px at 170px 120px, var(--leaf-mid) 0%, rgba(106,165,47,0) 100%),
      radial-gradient(ellipse 180px 220px at 50px 800px, var(--leaf-dark) 0%, rgba(47,95,34,0) 100%),
      radial-gradient(ellipse 520px 200px at 420px 1000px, var(--leaf-mid) 0%, rgba(106,165,47,0) 100%),
      radial-gradient(ellipse 200px 200px at 760px 760px, var(--leaf-light) 0%, rgba(166,210,74,0) 100%),
      radial-gradient(ellipse 240px 180px at 560px 640px, var(--sky-deep) 0%, rgba(58,98,200,0) 100%),
      linear-gradient(180deg, var(--sky-light) 0%, var(--sky-mid) 45%, var(--sky-deep) 80%);
  }
  .creature {
    position: absolute;
    left: 310px;
    top: 400px;
    width: 180px;
    height: 240px;
    border-radius: 50%;
    background:
      radial-gradient(ellipse 40px 55px at 52% 55%, var(--creature-gold) 0%, rgba(226,194,58,0) 100%),
      radial-gradient(ellipse 70px 100px at 52% 52%, var(--creature-dark) 0%, rgba(30,26,20,0.55) 55%, rgba(30,26,20,0) 100%);
  }
  .author {
    position: absolute;
    top: 78px;
    left: 0;
    width: 100%;
    text-align: center;
    font-size: 44px;
    font-weight: 400;
    letter-spacing: 0.2em;
    text-indent: 0.2em;
  }
  .title {
    position: absolute;
    left: 90px;
    top: 790px;
    width: 625px;
    font-family: "Archivo Black", "Arial Black", sans-serif;
    line-height: 1;
    text-shadow: 2px 3px 6px rgba(0, 0, 0, 0.35);
  }
  .title-line { display: block; white-space: nowrap; }
  .title-top { font-size: 67px; color: var(--white); }
  .title-bottom { font-size: 92px; color: var(--crimson); margin-top: 2px; }
  .title-tag {
    position: absolute;
    right: 92px;
    top: 920px;
    font-family: "Caveat", cursive;
    font-size: 52px;
    color: var(--white);
    line-height: 1;
  }
  .info-band {
    position: absolute;
    left: 0;
    bottom: 0;
    width: 100%;
    height: 153px;
    background: var(--crimson);
    text-align: center;
  }
  .tagline {
    padding-top: 18px;
    font-size: 26px;
    line-height: 33px;
    letter-spacing: 0.14em;
  }
  .website {
    margin-top: 17px;
    font-size: 20px;
    letter-spacing: 0.16em;
  }
</style>
</head>
<body>
  <main class="cover">
    <div class="cover-art" role="img" aria-label="Painted view up through green leaves to a blue sky, with a fine orb web stretched across the centre"></div>
    <div class="creature" role="img" aria-label="Black and yellow garden creature resting at the centre of the web"></div>

    <p class="author">Dale Prowse</p>

    <h1 class="title">
      <span class="title-line title-top">MOTHS BEYOND</span>
      <span class="title-line title-bottom">THE HEDGE</span>
    </h1>
    <p class="title-tag">a pocket handbook</p>

    <footer class="info-band">
      <p class="tagline">An easy to understand identification guide<br>with plenty of tips and illustrations</p>
      <p class="website">Brindlewing.com</p>
    </footer>
  </main>
</body>
</html>
```